Glow and Petal med spa needs an awesome eye catching billboard ad

We need a billboard ad design for a Med Spa with location sin Davenport and Windermere FL A medical spa where the beauty of nature meets the power of science to treat the whole person, mind, body and soul.

Meadowlight Renewal Med Spa is a medical spa where the beauty of nature meets the power of science to create gorgeous, youthful looking skin. Located in Davenport, Florida, but also serving Four Corners, Celebration, and Windermere, Florida, the talented professional team brings decades of experience in world-class skin care to provide holistic, science-backed aesthetic services and health coaching.

Industry/Entity Type

Spa

Colors
fbee3e
fece3e
eea4c8
e667a6
fbee3d

Requirements
Must have
• Locations in Davenport and Dr Phillips
Phone 407-555-0192
website www.glowandpetal.example

Boards for each:
Aesthetic Treatments
Cosmetic Injectables
Lumora facial
add color vs too many earthtones, to catch the eye perhaps using yellow, something that catches the eye and stands out from the normal everyday
Thank you!!!!
Nice to have
• Boards for each:
Aesthetic Treatments
Cosmetic Injectables
Lumora facial
add color vs too many earthtones, to catch the eye
photos that match services,
Thank you!!!!

```html
<!DOCTYPE html>
<html lang="en">
<head>
<meta charset="utf-8">
<title>Meadowlight Renewal Med Spa – Cosmetic Injectables Billboard</title>
<link rel="stylesheet" href="https://fonts.googleapis.com/css2?family=Montserrat:wght@400;500;600;700&display=swap">
<style>
  :root {
    --gold: #cdb783;
    --charcoal: #3b3b3c;
    --ink: #1f1f21;
    --white: #ffffff;
    --photo-light: #eceef1;
    --photo-mid: #cfd2d6;
    --skin: #efd2c2;
    --stage: #e6e6e6;
  }
  html, body {
    margin: 0;
    width: 1000px;
    height: 1200px;
    overflow: hidden;
    background: var(--stage);
    font-family: "Montserrat", sans-serif;
  }
  .billboard {
    position: absolute;
    left: 20px;
    top: 420px;
    width: 960px;
    height: 360px;
    background: var(--white);
    overflow: hidden;
    box-shadow: 0 6px 24px rgba(0,0,0,0.15);
  }
  .hero-photo {
    position: absolute;
    left: 356px;
    top: 0;
    width: 604px;
    height: 286px;
    background:
      radial-gradient(ellipse 120px 150px at 440px 150px, var(--skin) 0%, rgba(239,210,194,0.4) 55%, rgba(239,210,194,0) 100%),
      linear-gradient(100deg, var(--photo-mid) 0%, var(--photo-light) 70%, #d9dce0 100%);
  }
  .curves {
    position: absolute;
    inset: 0;
  }
  .brand {
    position: absolute;
    left: 42px;
    top: 46px;
    display: flex;
    align-items: center;
    gap: 14px;
  }
  .brand-dot {
    width: 58px;
    height: 58px;
    border-radius: 50%;
    background: var(--gold);
  }
  .brand-name {
    color: var(--gold);
    font-weight: 500;
    font-size: 19px;
    letter-spacing: 4px;
    line-height: 1.35;
    text-transform: uppercase;
  }
  .headline {
    position: absolute;
    left: 62px;
    top: 142px;
    margin: 0;
    line-height: 1;
  }
  .headline-light {
    display: block;
    color: var(--gold);
    font-weight: 500;
    font-size: 60px;
    letter-spacing: -0.5px;
  }
  .headline-bold {
    display: block;
    color: var(--ink);
    font-weight: 700;
    font-size: 62px;
    margin-top: 2px;
  }
  .location-bar {
    position: absolute;
    left: 42px;
    top: 296px;
    height: 45px;
    display: flex;
    font-weight: 600;
    font-size: 21px;
    color: var(--white);
  }
  .location-label {
    background: var(--charcoal);
    padding: 0 17px;
    display: flex;
    align-items: center;
  }
  .location-places {
    background: var(--gold);
    padding: 0 26px;
    display: flex;
    align-items: center;
    width: 323px;
  }
  .contact-band {
    position: absolute;
    left: 648px;
    top: 286px;
    width: 312px;
    height: 74px;
    background: var(--charcoal);
    color: var(--white);
    text-align: center;
  }
  .contact-phone {
    display: block;
    font-weight: 700;
    font-size: 29px;
    letter-spacing: 1px;
    margin-top: 6px;
    line-height: 1.1;
  }
  .contact-web {
    display: block;
    font-weight: 500;
    font-size: 15px;
    letter-spacing: 0.5px;
    margin-top: 2px;
  }
  .contact-web .accent { color: var(--gold); }
</style>
</head>
<body>
  <section class="billboard" aria-label="Cosmetic injectables billboard">
    <div class="hero-photo" role="img" aria-label="Photo of a woman with smooth, glowing skin touching her face"></div>

    <svg class="curves" viewBox="0 0 960 360" width="960" height="360" aria-hidden="true">
      <path class="wave-gold" fill="#cdb783"
            d="M350,0 L374,0 C400,90 560,130 622,230 C646,272 652,320 652,360 L636,360 C636,340 632,315 620,290 C560,170 372,150 350,0 Z"/>
      <path class="wave-white" fill="#ffffff"
            d="M0,0 L350,0 C372,150 560,170 620,290 C632,315 636,340 636,360 L0,360 Z"/>
      <path class="wave-charcoal" fill="#3b3b3c"
            d="M378,62 C420,130 560,150 606,228 C622,256 626,292 622,326 C614,284 598,254 566,228 C498,174 396,142 378,62 Z"/>
    </svg>

    <div class="brand">
      <span class="brand-dot" aria-hidden="true"></span>
      <span class="brand-name">Meadowlight<br>Renewal Med Spa</span>
    </div>

    <h1 class="headline">
      <span class="headline-light">Cosmetic</span>
      <span class="headline-bold">INJECTABLES</span>
    </h1>

    <div class="location-bar">
      <span class="location-label">Located in</span>
      <span class="location-places">Davenport and Dr Phillips</span>
    </div>

    <div class="contact-band">
      <span class="contact-phone">407-555-0192</span>
      <span class="contact-web">www.<span class="accent">glowandpetal</span>.example</span>
    </div>
  </section>
</body>
</html>
```